Designing a website for Brightmoor Pest Services PTY LTD

Pest control company looking for someone to build an informative website containing services we offer and an online inquiry form.
Commercial premises - Specialising in - Rodent control, stored product pest control, flying insect control, ant, spider and insect control, Termite inspections and treatments. Termite management systems on a commercial scale.
Facilities we service
Commercial - shopping centres, transport facilities, restaurants, pubs, clubs, bars food manufacturing facilities.
Residential - Houses specialising in - Rodent, Ant, Spider, Cockroach and Termite control. Termite inspections, Pre - purchase inspections, Termite treatments, Termite management systems.
Target Market(s)
Mainly commercial and industrial clients and Residential clients.
Industry/Entity Type
Pest Control
Number of Pages Required
1 page
Look and feel

```html
<!DOCTYPE html>
<html lang="en">
<head>
<meta charset="utf-8">
<title>Brightmoor Pest Services</title>
<link rel="stylesheet" href="https://fonts.googleapis.com/css2?family=Oswald:wght@500;600&family=Roboto:wght@400;500;700&family=Poppins:wght@400;500&display=swap">
<style>
:root{
  --green:#3b9a13;
  --green-dark:#2f7f0c;
  --ink:#1a1a1a;
  --text:#444;
  --paper:#f6f6f6;
  --white:#fff;
  --footer:#1d1d1d;
  --line:#d9d9d9;
}
*{box-sizing:border-box;margin:0;padding:0}
html,body{width:1200px;height:5076px;overflow:hidden}
body{font-family:"Roboto",sans-serif;color:var(--text);background:var(--white);position:relative}
section,header,footer{position:absolute;left:0;width:1200px}
.abs{position:absolute}
.photo{position:absolute}
.eyebrow{font-family:"Roboto",sans-serif;font-weight:500;color:var(--green);font-size:18px;text-align:center;letter-spacing:.3px}
.title{font-family:"Oswald",sans-serif;font-weight:600;color:var(--ink);font-size:40px;text-align:center;letter-spacing:.3px}
.rule{width:50px;height:3px;background:var(--green);margin:8px auto 0}
.brand{font-family:"Oswald",sans-serif;font-weight:600;color:var(--ink);display:flex;align-items:center;gap:10px}
.brand .dot{width:16px;height:16px;border-radius:50%;background:var(--green)}

/* header */
.site-header{top:0;height:98px;background:var(--white)}
.site-header .brand{position:absolute;left:100px;top:24px;font-size:34px}
.nav{position:absolute;left:365px;top:58px;display:flex;gap:42px;font-size:14px;font-weight:700;color:var(--ink)}
.nav .active{color:var(--green)}
.header-call{position:absolute;left:910px;top:38px;width:290px;height:60px;background:var(--green);color:var(--white);display:flex;align-items:center;gap:14px;padding-left:0}
.header-call .ring{width:46px;height:46px;border-radius:50%;background:var(--ink);display:flex;align-items:center;justify-content:center;margin-left:-6px;border:4px solid var(--white)}
.header-call small{display:block;font-size:11px}
.header-call b{font-size:19px}

/* hero */
.hero{top:98px;height:607px}
.hero .photo{inset:0;background:linear-gradient(90deg,#6d6f72 0%,#b9bcbf 35%,#d8d9db 60%,#8f9296 100%)}
.hero h1{position:absolute;left:96px;top:262px;font-family:"Oswald",sans-serif;font-weight:600;font-size:46px;line-height:1.12;color:var(--ink)}
.hero p{position:absolute;left:98px;top:382px;font-size:18px;color:var(--ink)}
.btn{display:inline-block;background:var(--green);color:var(--white);font-weight:700;font-size:14px;text-transform:uppercase}
.hero .btn{position:absolute;left:98px;top:428px;padding:14px 26px}
.appointment{position:absolute;left:786px;top:0;width:312px;height:607px;background:var(--green);padding:20px 14px 0}
.appointment h2{color:var(--white);text-align:center;font-family:"Oswald",sans-serif;font-weight:500;line-height:1.1}
.appointment h2 small{display:block;font-size:20px;font-weight:400}
.appointment h2 span{font-size:32px}
.field{height:42px;background:var(--white);margin-top:9px;font-size:12px;color:#777;padding:13px 12px;position:relative}
.field.tall{height:86px}
.field .caret{position:absolute;right:12px;top:18px;border:5px solid transparent;border-top-color:#222}
.appointment .send{margin-top:16px;height:50px;background:var(--ink);color:var(--white);font-weight:700;font-size:14px;display:flex;align-items:center;justify-content:center}

/* story */
.story{top:705px;height:557px;background:var(--paper)}
.story .eyebrow{margin-top:70px}
.story .brand{justify-content:center;font-size:72px;margin-top:22px}
.story .brand .dot{width:30px;height:30px}
.story .title{margin-top:18px}
.story p{width:880px;margin:22px auto 0;text-align:center;font-size:14px;line-height:24px}

/* split */
.split{top:1262px;height:428px;overflow:hidden}
.split .left{left:0;top:0;width:590px;height:428px;background:linear-gradient(135deg,#e8e8e6,#b7b4ae)}
.split .right{left:590px;top:0;width:610px;height:428px;background:linear-gradient(135deg,#8b6a3d,#3d4c6b 70%,#1e2a45)}
.tag-res{left:180px;top:240px;width:330px;height:86px;background:var(--green);color:var(--white);font-family:"Roboto",sans-serif;font-weight:700;font-size:36px;display:flex;align-items:center;padding-left:54px;clip-path:polygon(14% 0,100% 0,100% 100%,0 100%)}
.tag-com{left:690px;top:110px;width:320px;height:86px;background:var(--ink);color:var(--white);font-weight:700;font-size:36px;display:flex;align-items:center;padding-left:62px;clip-path:polygon(0 0,100% 0,86% 100%,0 100%)}
.badge{left:455px;top:65px;width:290px;height:290px;border-radius:50%;background:var(--white);border:14px solid var(--green);border-right-color:var(--ink);border-top-color:var(--ink);display:flex;align-items:center;justify-content:center}
.badge .brand{font-size:40px}

/* services */
.services{top:1690px;height:665px}
.services .eyebrow{margin-top:90px}
.tabs{position:absolute;top:196px;left:316px;display:flex;gap:12px}
.tab{width:276px;height:48px;border:1px solid #bbb;font-weight:700;font-size:16px;display:flex;align-items:center;justify-content:center;color:var(--ink);position:relative}
.tab.on{background:var(--green);border-color:var(--green);color:var(--white)}
.tab.on:after{content:"";position:absolute;bottom:-10px;left:50%;margin-left:-10px;border:10px solid transparent;border-bottom:0;border-top-color:var(--green)}
.cards{position:absolute;top:280px;left:79px;display:flex;gap:10px}
.card{width:255px;height:339px;background:var(--white);box-shadow:0 2px 10px rgba(0,0,0,.14);text-align:center;position:relative}
.card .photo{position:relative;height:175px}
.card .icon{position:absolute;left:50%;top:142px;margin-left:-33px;width:66px;height:66px;border-radius:50%;background:var(--green);border:4px solid var(--white);display:flex;align-items:center;justify-content:center}
.card h3{margin-top:44px;font-size:18px;font-weight:500;color:var(--ink);line-height:20px;min-height:40px;display:flex;align-items:flex-end;justify-content:center;padding:0 10px}
.card p{font-size:13px;line-height:21px;margin:8px 14px 0}

/* facilities */
.facilities{top:2355px;height:877px}
.facilities .eyebrow{margin-top:58px}
.tile{position:absolute;width:324px;height:305px;display:flex;align-items:flex-end;justify-content:center;padding-bottom:22px;color:var(--white);font-weight:500;font-size:18px}

/* why */
.why{top:3232px;height:685px;background:var(--white)}
.why .eyebrow{margin-top:92px}
.why-ring{left:396px;top:216px;width:414px;height:414px;border-radius:50%;border:12px solid #eef6ea}
.why .center{left:500px;top:360px;width:230px;height:130px;display:flex;align-items:center;justify-content:center}
.why .center .brand{font-size:46px}
.point{position:absolute;display:flex;align-items:center;gap:18px;font-size:19px;color:var(--ink);line-height:24px}
.point .ico{width:86px;height:86px;border-radius:50%;background:var(--green);border:8px solid #e6f2df;display:flex;align-items:center;justify-content:center;flex:none}
.point.l{text-align:right;justify-content:flex-end}

/* testimonial */
.testimonial{top:3917px;height:433px;overflow:hidden}
.testimonial .photo{left:0;top:0;width:700px;height:433px;background:linear-gradient(120deg,#e8ecef,#c2ccd4)}
.testimonial .panel{position:absolute;left:555px;top:0;width:645px;height:433px;background:var(--green);clip-path:polygon(13% 0,100% 0,100% 100%,0 100%)}
.quote{left:560px;top:172px;width:78px;height:78px;border-radius:50%;background:var(--ink);border:5px solid var(--white)}
.testimonial .copy{position:absolute;left:660px;top:72px;width:420px;text-align:center;color:var(--white)}
.testimonial .copy em{font-family:"Oswald",sans-serif;font-size:20px;font-weight:500}
.testimonial .copy h2{font-family:"Oswald",sans-serif;font-weight:600;font-size:44px;margin-top:8px}
.testimonial .copy p{font-size:14px;line-height:26px;margin-top:14px}
.testimonial .copy b{display:block;margin-top:16px;font-size:17px}
.arrows{display:flex;gap:6px;justify-content:center;margin-top:26px}
.arrows span{width:34px;height:28px;border:1px solid var(--white)}

/* cta */
.cta{top:4350px;height:324px}
.cta .frame{left:232px;top:118px;width:736px;height:110px;border:2px solid var(--ink)}
.cta .frame:before{content:"";position:absolute;inset:6px;border:1px solid var(--ink)}
.cta .label{left:526px;top:100px;width:148px;height:34px;background:var(--ink);color:var(--white);font-weight:700;font-size:14px;display:flex;align-items:center;justify-content:center}
.cta h2{position:absolute;left:232px;top:148px;width:736px;text-align:center;font-family:"Oswald",sans-serif;font-weight:500;font-size:36px;color:var(--ink)}
.cta .btn{position:absolute;left:440px;top:210px;width:320px;height:44px;display:flex;align-items:center;justify-content:center;font-size:15px}

/* footer */
.site-footer{top:4674px;height:402px;background:var(--footer);color:#ddd}
.site-footer .brand{position:absolute;left:96px;top:100px;color:var(--white);font-size:40px}
.site-footer h4{font-family:"Roboto",sans-serif;font-weight:500;font-size:17px;color:var(--white);margin-bottom:14px}
.col{position:absolute;top:106px;font-size:13px;line-height:28px}
.contact-row{display:flex;gap:12px;line-height:20px;margin-bottom:12px}
.social{display:flex;gap:8px}
.social span{width:38px;height:38px;border-radius:50%;border:1px solid #aaa}
.copyright{position:absolute;left:0;right:0;bottom:20px;text-align:center;font-size:13px;border-top:1px solid #444;margin:0 80px;padding-top:20px}
</style>
</head>
<body>

<header class="site-header">
  <div class="brand"><span class="dot"></span>Brightmoor</div>
  <nav class="nav"><span class="active">HOME</span><span>ABOUT</span><span>SERVICES</span><span>TESTIMONIAL</span><span>CONTACT US</span></nav>
  <div class="header-call">
    <div class="ring"><svg width="20" height="20" viewBox="0 0 24 24"><path fill="#fff" d="M6.6 10.8a15 15 0 0 0 6.6 6.6l2.2-2.2c.3-.3.7-.4 1-.2 1.1.4 2.3.6 3.6.6.6 0 1 .4 1 1V20c0 .6-.4 1-1 1A17 17 0 0 1 3 4c0-.6.4-1 1-1h3.5c.6 0 1 .4 1 1 0 1.3.2 2.5.6 3.6.1.3 0 .7-.2 1z"/></svg></div>
    <div><small>FREE CONSULTATION</small><b>(555)010-2480</b></div>
  </div>
</header>

<section class="hero">
  <div class="photo" role="img" aria-label="Technicians in white protective suits spraying and wiping a living room"></div>
  <h1>RESIDENTIAL &amp; COMMERCIAL<br>PEST SOLUTIONS</h1>
  <p>LOREM IPSUM DOLOR SIT AMET, CONSECTETUR ADI</p>
  <span class="btn">Call us today for a free quote</span>
  <form class="appointment">
    <h2><small>SCHEDULE AN</small><span>APPOINTMENT</span></h2>
    <div class="field">Name</div>
    <div class="field">Email</div>
    <div class="field">Phone</div>
    <div class="field">Services<span class="caret"></span></div>
    <div class="field">Address</div>
    <div class="field tall">Message</div>
    <div class="send">SEND YOUR MESSAGE</div>
  </form>
</section>

<section class="story">
  <div class="eyebrow">OUR STORY</div>
  <div class="brand"><span class="dot"></span>Brightmoor</div>
  <h2 class="title">ANYTIME, ANYWHERE BRIGHTMOOR WILL BE THERE</h2>
  <div class="rule"></div>
  <p>Lorem ipsum dolor sit amet, consectetur adipiscing elit, sed sumod tempor incididunt ut labore et dolore magna aliqua. Qupsum suspendisse ultrices gravida. Risus commodo viverra maecenas accumsan lacus veilisis. Lorem ipsum dolor sit amet, consectetur adipiscing elit, sed do eempor incididunt ut labore et dolore magna aliqua. Lorem ipsum dolor sit amet, consectetur adipiscing elit, sed sumod tempor incididunt ut labore et dolore magna aliqua. Qupsum suspendisse ultrices gravida. Risus commodo viverra maecenas</p>
</section>

<section class="split">
  <div class="photo left" role="img" aria-label="Technicians treating a home interior"></div>
  <div class="photo right" role="img" aria-label="Technician spraying a warehouse full of stored goods"></div>
  <div class="abs tag-res">Residential</div>
  <div class="abs tag-com">Commercial</div>
  <div class="abs badge"><div class="brand"><span class="dot"></span>Brightmoor</div></div>
</section>

<section class="services">
  <div class="eyebrow">OUR SERVICES</div>
  <h2 class="title">WHAT WE DO</h2>
  <div class="rule"></div>
  <div class="tabs"><div class="tab on">RESIDENTIAL SERVICES</div><div class="tab">COMMERCIAL SERVICES</div></div>
  <div class="cards">
    <article class="card">
      <div class="photo" role="img" aria-label="Technician inspecting a floor with cockroaches" style="background:linear-gradient(135deg,#e9e6e2,#bdb6ad)"></div>
      <div class="icon"><svg width="30" height="30" viewBox="0 0 24 24" fill="none" stroke="#fff" stroke-width="1.8"><circle cx="12" cy="13" r="4"/><path d="M12 9V5M8 11 4 8M16 11l4-3M8 15l-4 3M16 15l4 3"/></svg></div>
      <h3>ANTS, COCKROACHES, SPIDERS</h3>
      <p>Lorem ipsum dolor set, consectetur adipiscing elit, sed do smod tempor incididunt ut labore et</p>
    </article>
    <article class="card">
      <div class="photo" role="img" aria-label="Technician spraying a kitchen" style="background:linear-gradient(135deg,#3c3d40,#a6a7a9)"></div>
      <div class="icon"><svg width="30" height="30" viewBox="0 0 24 24" fill="none" stroke="#fff" stroke-width="1.8"><ellipse cx="11" cy="14" rx="7" ry="4.5"/><circle cx="15" cy="9" r="2"/><path d="M4 15c-2 1-2 3 0 4"/></svg></div>
      <h3>RODENT CONTROL</h3>
      <p>Lorem ipsum dolor set, consectetur adipiscing elit, sed do smod tempor incididunt ut labore et</p>
    </article>
    <article class="card">
      <div class="photo" role="img" aria-label="Inspector crawling under a timber floor" style="background:linear-gradient(135deg,#8a5a2c,#d7b27a)"></div>
      <div class="icon"><svg width="30" height="30" viewBox="0 0 24 24" fill="none" stroke="#fff" stroke-width="2"><circle cx="14" cy="10" r="5.5"/><path d="M10 14 4 20"/></svg></div>
      <h3>TERMITE INSPECTIONS</h3>
      <p>Lorem ipsum dolor set, consectetur adipiscing elit, sed do smod tempor incididunt ut labore et</p>
    </article>
    <article class="card">
      <div class="photo" role="img" aria-label="Two technicians reviewing a clipboard" style="background:linear-gradient(135deg,#cfd3d6,#7b8a94)"></div>
      <div class="icon"><svg width="30" height="30" viewBox="0 0 24 24" fill="none" stroke="#fff" stroke-width="1.8"><path d="M3 11 12 4l9 7M6 9v11h12V9M10 20v-6h4v6"/></svg></div>
      <h3>TERMITE TREATMENTS &amp; MANAGEMENT SYSTEMS</h3>
      <p>Lorem ipsum dolor set, consectetur adipiscing elit, sed do smod tempor incididunt ut labore et</p>
    </article>
  </div>
</section>

<section class="facilities">
  <div class="eyebrow">SERVICE AREA</div>
  <h2 class="title">FACILITIES WE SERVICE</h2>
  <div class="rule"></div>
  <div class="tile" role="img" aria-label="Food production line" style="left:100px;top:157px;background:linear-gradient(180deg,#9aa0a3,#4d4f4e)">FOOD MANUFACTURING FACILITIES</div>
  <div class="tile" role="img" aria-label="Bus interior being sprayed" style="left:438px;top:157px;background:linear-gradient(180deg,#c9cfd6,#2c3f70)">TRANSPORT FACILITIES</div>
  <div class="tile" role="img" aria-label="Restaurant dining room" style="left:776px;top:157px;background:linear-gradient(180deg,#5a4a3a,#2a241e)">RESTAURANTS</div>
  <div class="tile" role="img" aria-label="Pub bar with beer taps" style="left:100px;top:478px;background:linear-gradient(180deg,#5c3b22,#1b1411)">PUBS</div>
  <div class="tile" role="img" aria-label="Night club bar lit in purple" style="left:438px;top:478px;background:linear-gradient(180deg,#3d2f6e,#141228)">CLUBS</div>
  <div class="tile" role="img" aria-label="Shopping centre walkway" style="left:776px;top:478px;background:linear-gradient(180deg,#e0c8a8,#7d7a74)">SHOPPING CENTRES</div>
</section>

<section class="why">
  <div class="eyebrow">WHY CHOOSE US</div>
  <h2 class="title">WHY CHOOSE BRIGHTMOOR PEST SERVICES?</h2>
  <div class="rule"></div>
  <div class="abs why-ring"></div>
  <div class="abs center"><div class="brand"><span class="dot"></span>Brightmoor</div></div>
  <div class="point l" style="right:710px;top:217px"><span>Focusing on your<br>needs</span><span class="ico"><svg width="30" height="30" viewBox="0 0 24 24" fill="none" stroke="#fff" stroke-width="1.8"><circle cx="8" cy="8" r="3"/><circle cx="16" cy="8" r="3"/><path d="M3 20c0-4 2-6 5-6s5 2 5 6M11 20c0-4 2-6 5-6s5 2 5 6"/></svg></span></div>
  <div class="point l" style="right:740px;top:340px"><span>Cost Effective Options<br>Available</span><span class="ico"><svg width="30" height="30" viewBox="0 0 24 24" fill="none" stroke="#fff" stroke-width="1.8"><circle cx="12" cy="9" r="5"/><path d="M3 19h13l5-3"/></svg></span></div>
  <div class="point l" style="right:740px;top:462px"><span>Residential &amp;<br>Commercial</span><span class="ico"><svg width="30" height="30" viewBox="0 0 24 24" fill="none" stroke="#fff" stroke-width="1.8"><path d="M5 21V5h8v16M13 10h6v11M3 21h18M8 8h2M8 12h2M8 16h2"/></svg></span></div>
  <div class="point" style="left:745px;top:217px"><span class="ico"><svg width="30" height="30" viewBox="0 0 24 24" fill="#fff"><path d="M12 3l2.6 5.3 5.9.8-4.3 4.1 1 5.8L12 16.3 6.8 19l1-5.8-4.3-4.1 5.9-.8z"/></svg></span><span>100% Satisfaction<br>Guarantee</span></div>
  <div class="point" style="left:760px;top:340px"><span class="ico"><svg width="30" height="30" viewBox="0 0 24 24" fill="none" stroke="#fff" stroke-width="2"><circle cx="12" cy="12" r="8"/><path d="m8 12 3 3 5-6"/></svg></span><span>Family owned and<br>operated</span></div>
  <div class="point" style="left:760px;top:462px"><span class="ico"><svg width="30" height="30" viewBox="0 0 24 24" fill="none" stroke="#fff" stroke-width="1.8"><path d="M4 12a8 8 0 1 0 3-6M4 4v4h4"/><path d="M12 8v4l3 2"/></svg></span><span>Call or Chat with us<br>Anytime</span></div>
</section>

<section class="testimonial">
  <div class="photo" role="img" aria-label="Happy couple holding house keys"></div>
  <div class="panel"></div>
  <div class="abs quote"></div>
  <div class="copy">
    <em>WHAT OUR CUSTOMERS SAY</em>
    <h2>SATISFIED CLIENTS</h2>
    <p>Lorem ipsum dolor sit amet, consectetur adipiscing elit, sed do eiusmod tempor incididunt ut labore et dolore a aliqua. Quis ipsum susse ultrices gravida. Risus commodo</p>
    <b>SAM CARTER</b>
    <div class="arrows"><span></span><span></span></div>
  </div>
</section>

<section class="cta">
  <div class="abs frame"></div>
  <div class="abs label">CONTACT US</div>
  <h2>CALL NOW FOR BRIGHTMOOR PEST SERVICES TODAY</h2>
  <span class="btn">Call us today at (555)010-2480 ›</span>
</section>

<footer class="site-footer">
  <div class="brand"><span class="dot"></span>Brightmoor</div>
  <div class="col" style="left:398px"><h4>QUICK LINK</h4>Home<br>Our Services<br>About Us<br>Why Choose Us<br>FAQ's<br>Contact Us</div>
  <div class="col" style="left:612px"><h4>CONTACT US</h4>
    <div class="contact-row"><svg width="14" height="18" viewBox="0 0 24 24" fill="#fff"><path d="M12 2a7 7 0 0 0-7 7c0 5 7 13 7 13s7-8 7-13a7 7 0 0 0-7-7zm0 9.5A2.5 2.5 0 1 1 12 6.5a2.5 2.5 0 0 1 0 5z"/></svg><span>48 Example Lane Springfield<br>20100</span></div>
    <div class="contact-row"><svg width="14" height="18" viewBox="0 0 24 24" fill="#fff"><path d="M2 5h20v14H2zm2 2 8 6 8-6"/></svg><span>Email:<br>hello@brightmoorpest.example</span></div>
    <div class="contact-row"><svg width="14" height="18" viewBox="0 0 24 24" fill="#fff"><path d="M6.6 10.8a15 15 0 0 0 6.6 6.6l2.2-2.2c.3-.3.7-.4 1-.2 1.1.4 2.3.6 3.6.6.6 0 1 .4 1 1V20c0 .6-.4 1-1 1A17 17 0 0 1 3 4c0-.6.4-1 1-1h3.5c.6 0 1 .4 1 1 0 1.3.2 2.5.6 3.6.1.3 0 .7-.2 1z"/></svg><span>Phone:<br>(555) 010 2480</span></div>
  </div>
  <div class="col" style="left:925px"><h4>FOLLOW US</h4><div class="social"><span></span><span></span><span></span><span></span></div></div>
  <div class="copyright">Copyright © 2021 Brightmoor Pest Services PTY LTD. All rights</div>
</footer>

</body>
</html>
```